Velvet Larks website

Home page and info page design needed
PRODUCTION NOTES

* 10 Page Website
* Blog

CLIENT PURPOSE

• Provide information not easily/commonly available for women over 40
• Focus on unusual opportunities
• Fun / Informative / Unique / Helpful

PLATFORM
Wordpress

SERVICES
Inform / Encourage / Emphasise - Information / Topics etc -
Promote products for the over 40’s - From advertisers etc. -
- -

COMPETITION
Cycle Compass - cyclecompass.co.uk
Kinfolk Hub - kinfolkhub.com
Stay Spry Past Sixty - stayspryspastsixty.com

WEBSITE(S) CLIENT LIKES
kinfolkhub.com
ladytinkerstyle.com
qvn.co.uk
tallowbrook.org.uk

WEBSITE CLIENT DOES NOT LIKE
cyclecompass.co.uk

COMPANY LOGO
Customer has a company logo - their existing site is here http://velvetlarks.com - this is the logo you should use , you need to reflect the feel of the logo throughout the whole design

COLOURS:
as the logo

STRAPLINE:
Dangerously Fascinating Women

EMAIL ADDRESSES TO APPEAR ON WEBSITE:
info@velvetlarks.com -

WEBSITE THEME:
Womens Health

IMAGES THAT BEST REFLECT YOUR COMPANY: •
Retro / Funky / Unusual / Eye-catching• As per original site but more sophisticated•
Focus groups said they liked style/look of old site but thought it looked a bit ‘young’ for target group

HEADER IMAGE:
Women - Active

PAGES:
Home
About Us
Explore Something New
Health & Well Being –
Relationships
Blog
Mind, Body & Soul
Contact

MESSAGE BANNERS:

Need to show recent Blog entries.-Maybe have TOP 5 related issues?
* Boost your sex drive.
* What is HRT? * Suffering from migraines?
* Treatment Options
* Do symptoms get worse when you start on HRT?-Picture of Fenella & Morwen‘ Written by like minded women’
Link to blog entry about the founders of the website?-Maybe a Product option?Advertising option...-Your story..

USER JOURNEYS:

General Service > Land on website > Service Banners > Info Pages > Contact FormQuestions > Land on website > Message Banners > Info Pages > Contact FormContact > Land on website > Clear Telephone / Email Banner > Contact Form

CALL TO ACTION BANNER:

Search the blog..

-

KEYWORDS THAT RELATE TO YOUR BUSINESS:

Menopause
Hormones
Mid Life
Stress
Empty Nest
Womans Health
HRT
Body & Soul
hormone replacement therapy

LOCATION(S):

United Kingdom -

here is the link to the clients current site
http://velvetlarks.com/index.html

Target Market(s)

woman over 40+

Industry/Entity Type

Consulting

Number of Pages Required

1 page

Requirements
Must have
• take the colours and style of the logo and use throughout the design
Should not have
• Cliche pictures of older woman - you need to give the right balance of seriousness and fun - must not come accross as boring BUT also not too light hearted

```html
<!DOCTYPE html>
<html lang="en">
<head>
<meta charset="utf-8">
<title>Velvet Larks – Dangerously Fascinating Women</title>
<link href="https://fonts.googleapis.com/css2?family=Francois+One&family=Open+Sans:wght@400;600&family=Ubuntu:wght@400;500;700&display=swap" rel="stylesheet">
<style>
:root{
  --plum:#650b60;
  --plum-deep:#2b0429;
  --plum-light:#9a3d92;
  --magenta:#c0199e;
  --magenta-light:#e04bc2;
  --heading:#8b3b7e;
  --accent-red:#e3334f;
  --text:#555;
  --panel-border:#e6e6e6;
  --rule:#dcdcdc;
  --footer-text:#f3dcf0;
  --button:#c45cc1;
  --ornament:#c763b9;
}
*{box-sizing:border-box;margin:0;padding:0}
html,body{width:738px;height:1200px;overflow:hidden}
body{font-family:"Open Sans",sans-serif;color:var(--text)}
.page{position:relative;width:738px;height:1200px;overflow:hidden;
  background:radial-gradient(ellipse 260px 200px at 250px 60px,#9d4c98 0%,rgba(157,76,152,0) 100%),
  linear-gradient(#6c1068,#5e0a5a 60%,#640d60)}
.top-strip{position:absolute;left:0;top:0;width:738px;height:8px;background:#5a0a56}
.social{position:absolute;top:9px;display:flex;gap:12px;left:602px}
.social span{display:block;width:17px;height:17px;border-radius:2px;background:#8a5585}
.brand{position:absolute;left:55px;top:24px;display:flex;align-items:center;gap:8px}
.brand-dot{width:30px;height:30px;border-radius:50%;background:var(--magenta-light)}
.brand-name{font-family:"Ubuntu",sans-serif;font-weight:700;font-size:27px;color:#f4b8ec}
.strapline{position:absolute;left:98px;top:72px;font-family:"Open Sans",sans-serif;font-weight:600;font-size:7px;color:#fff}
.promo{position:absolute;left:395px;top:37px;width:284px;height:43px;background:#f5f6f8;border:1px solid #ddd;text-align:center;overflow:hidden}
.promo-visual{position:absolute;left:117px;top:0;width:48px;height:12px;background:linear-gradient(#c9ccd0,#eef0f2)}
.promo-title{margin-top:14px;font-family:"Open Sans",sans-serif;font-size:13px;color:#4a8ec6;letter-spacing:.3px;line-height:1}
.promo-sub{font-size:5.5px;color:#333;margin-top:2px}
.main-nav{position:absolute;left:55px;top:94px;width:624px;height:33px;background:linear-gradient(#d43bb3,#b3128f);border:2px solid #7e1575;display:flex;align-items:center}
.main-nav a{font-family:"Ubuntu",sans-serif;font-size:9.5px;color:#fff;text-decoration:none;letter-spacing:.6px;margin-right:16px}
.main-nav a.active{height:35px;margin:-2px 8px -2px -2px;padding:0 11px;display:flex;align-items:center;background:linear-gradient(#e35cc8,#c0199e);border:2px solid #e887d6;box-shadow:0 2px 3px rgba(0,0,0,.35)}
.search{position:absolute;right:10px;top:6px;width:135px;height:19px;background:linear-gradient(#fafafa,#e9e9e9);border-radius:2px}
.search svg{position:absolute;right:6px;top:4px}
.panel{position:absolute;background:#fff;border:3px solid var(--panel-border)}
.widget{padding:0 10px 0 10px}
.widget-head{position:relative;height:27px;border-bottom:1px solid var(--rule);margin-left:18px;display:flex;align-items:center}
.widget-head h2{font-family:"Francois One",sans-serif;font-weight:400;font-size:11px;color:var(--heading);letter-spacing:.2px;padding-left:8px}
.ornament{position:absolute;left:-6px;top:-4px;width:30px;height:30px;border-radius:50%;background:var(--ornament)}
.feed{position:absolute;right:0;top:10px;width:8px;height:8px;border-radius:1px;background:#f08a3c}
.entry{padding:7px 0 6px;border-bottom:1px solid var(--rule);font-size:7.2px;line-height:8.5px;letter-spacing:.2px}
.entry:last-child{border-bottom:none}
.more{display:block;text-align:right;color:var(--accent-red);margin-top:1px}
.hero{left:211px;top:143px;width:311px;height:156px;padding:2px}
.hero-photo{position:relative;width:100%;height:100%;background:radial-gradient(circle at 60% 45%,#d9a587,#9a6649 55%,#3d2a22)}
.hero-quote{position:absolute;left:9px;bottom:11px;font-family:"Francois One",sans-serif;font-size:12px;line-height:13px;color:#fff;text-shadow:0 1px 2px rgba(0,0,0,.6)}
.tag-cloud{padding:9px 0 0;text-align:center;font-size:9px;line-height:12.5px;color:#222}
.tag-cloud b{font-weight:600;color:#000}
.articles{left:211px;top:308px;width:311px;height:570px;padding:0 10px}
.article{height:108px}
.article-head{display:flex;justify-content:space-between;align-items:baseline;border-bottom:1px solid var(--rule);padding:6px 0 4px}
.article-head h2{font-family:"Francois One",sans-serif;font-weight:400;font-size:13.5px;color:var(--heading)}
.article-head time{font-size:7px;color:var(--accent-red)}
.article p{font-size:7px;line-height:8.5px;letter-spacing:.15px;margin-top:6px}
.article p+p{margin-top:0}
.btn{display:block;width:52px;height:17px;margin:5px 2px 0 auto;border-radius:2px;background:linear-gradient(#d57ad2,#b64cb3);border:1px solid #9b3598;color:#fff;font-size:7px;font-style:italic;text-align:center;line-height:15px}
.article-long{height:auto}
.ad-slot{margin-top:9px;height:130px;background:linear-gradient(90deg,#c9d4dc,#eef2f5 45%,#dfe8f1)}
.site-footer{position:absolute;left:0;top:891px;width:738px;height:229px;background:radial-gradient(ellipse 330px 200px at 380px 130px,#9a4a92,#7a2872 70%,#6e1e67)}
.footer-base{position:absolute;left:0;top:1120px;width:738px;height:80px;background:var(--plum-deep)}
.footer-col{position:absolute;top:14px;width:148px}
.footer-col h3{font-family:"Francois One",sans-serif;font-weight:400;font-size:12.5px;color:#fff;padding-bottom:3px;border-bottom:1px dashed #d9a8d3;letter-spacing:.2px}
.footer-col ul{list-style:none;margin-top:8px}
.footer-col li,.footer-col p{font-family:"Ubuntu",sans-serif;font-size:8px;line-height:13px;color:var(--footer-text);letter-spacing:.3px}
.footer-col p{margin-top:8px}
</style>
</head>
<body>
<div class="page">
  <div class="top-strip"></div>
  <div class="social"><span></span><span></span><span></span></div>

  <header>
    <div class="brand"><span class="brand-dot"></span><span class="brand-name">Velvet Larks</span></div>
    <div class="strapline">Dangerously Fascinating Women</div>
    <div class="promo">
      <div class="promo-visual" role="img" aria-label="Product bottles"></div>
      <div class="promo-title">PERFECT BODY</div>
      <div class="promo-sub">The future of your body starts today.</div>
    </div>
  </header>

  <nav class="main-nav">
    <a class="active" href="#">MIND &amp; BODY</a>
    <a href="#">WOMENS HEALTH</a>
    <a href="#">RELATIONSHIPS</a>
    <a href="#">COMPANY NEWS</a>
    <div class="search">
      <svg width="11" height="11" viewBox="0 0 11 11"><circle cx="4" cy="4" r="3" fill="none" stroke="#333" stroke-width="1.4"/><line x1="6.2" y1="6.2" x2="10" y2="10" stroke="#333" stroke-width="2"/></svg>
    </div>
  </nav>

  <!-- Left column -->
  <section class="panel widget" style="left:55px;top:143px;width:148px;height:156px">
    <div class="widget-head"><span class="ornament" role="img" aria-label="Swirl ornament" style="left:-30px"></span><h2>Your Stories</h2><span class="feed"></span></div>
    <div class="entry">Morbi rhoncus arcu egestas erat, convallis<span class="more">Read More »</span></div>
    <div class="entry">Morbi rhoncus arcu egestas erat, convallis<span class="more">Read More »</span></div>
    <div class="entry">Morbi rhoncus arcu egestas erat, convallis<span class="more">Read More »</span></div>
  </section>

  <section class="panel widget" style="left:55px;top:308px;width:148px;height:190px">
    <div class="widget-head"><span class="ornament" role="img" aria-label="Swirl ornament" style="left:-30px"></span><h2>New Experiences</h2><span class="feed"></span></div>
    <div class="entry">A cras tincidunt, ut tellus et.<span class="more">Read More »</span></div>
    <div class="entry">Gravida scelerisque, ipsum sed iaculis, nunc non nam.<span class="more">Read More »</span></div>
    <div class="entry">In id, mauris viverra asperiores, bibendum in id.<span class="more">Read More »</span></div>
    <div class="entry">Wisi sodales nibh, quis lectus, sollicitudin pede morbi.<span class="more">Read More »</span></div>
  </section>

  <section class="panel widget" style="left:55px;top:508px;width:148px;height:172px">
    <div class="widget-head"><span class="ornament" role="img" aria-label="Swirl ornament" style="left:-30px"></span><h2>News</h2><span class="feed"></span></div>
    <div class="entry" style="padding-top:10px">Lorem ipsum dico oblique vis ex, pro id eruditi inermis, ei augue melius delicatissimi eos. Duo autem quaeque urbanitas an, ipsum intellegat ad cum.<span class="more">Read More »</span></div>
    <div class="entry">Lorem ipsum dico oblique vis ex, pro id eruditi inermis, ei augue melius delicatissimi eos. Duo autem quaeque urbanitas an, ipsum intellegat ad cum.<span class="more">Read More »</span></div>
  </section>

  <section class="panel widget" style="left:55px;top:688px;width:148px;height:190px">
    <div class="widget-head" style="flex-direction:column;align-items:flex-start;justify-content:center"><span class="ornament" role="img" aria-label="Swirl ornament" style="left:-30px"></span><h2 style="line-height:11px">About us</h2><span style="font-family:'Francois One',sans-serif;font-size:7px;color:var(--heading);padding-left:7px;line-height:8px">the original sirens</span></div>
    <div class="entry" style="padding-top:5px">Between us we tick all the boxes on the previous pages and, having spoken to friends and colleagues, know that there are thousands of other women just like us.<br>We haven't got all the answers but one thing we do know is that it helps to have friends - friends that you can honestly talk to about how you feel and what you are going through.<br>But how many friends like that do we really have and how often can you lean on them?<span class="more" style="margin-top:4px">Read More »</span></div>
  </section>

  <!-- Centre column -->
  <section class="panel hero">
    <div class="hero-photo" role="img" aria-label="Smiling woman, active lifestyle header photo">
      <div class="hero-quote">“When you have finished changing,<br>your through...”</div>
    </div>
  </section>

  <main class="panel articles">
    <article class="article">
      <div class="article-head"><h2>What is “The Menopause”</h2><time>25.03.2010</time></div>
      <p>A cras tincidunt, ut tellus et. Gravida scelerisque, ipsum sed iaculis, nunc non nam. Placerat sed phasellus, purus purus elit. Cras ante eros. Erat vel. Donec vestibulum sed, vel euismod donec.</p>
      <p>Eros ante malesuada. Pellentesque senectus, a tempor et. At pellentesque. Molestie in, nonummy libero, justo eros pariatur. Tortor sed. A ac.</p>
      <p>In id, mauris viverra asperiores, bibendum in id.</p>
      <a class="btn">Read More</a>
    </article>
    <article class="article">
      <div class="article-head"><h2>Mind Body &amp; HRT</h2><time>25.03.2010</time></div>
      <p>A cras tincidunt, ut tellus et. Gravida scelerisque, ipsum sed iaculis, nunc non nam. Placerat sed phasellus, purus purus elit. Cras ante eros. Erat vel. Donec vestibulum sed, vel euismod donec.</p>
      <p>Eros ante malesuada. Pellentesque senectus, a tempor et. At pellentesque. Molestie in, nonummy libero, justo eros pariatur. Tortor sed. A ac.</p>
      <p>In id, mauris viverra asperiores, bibendum in id.</p>
      <a class="btn">Read More</a>
    </article>
    <article class="article">
      <div class="article-head"><h2>Siren Sphere</h2><time>25.03.2010</time></div>
      <p>A cras tincidunt, ut tellus et. Gravida scelerisque, ipsum sed iaculis, nunc non nam. Placerat sed phasellus, purus purus elit. Cras ante eros. Erat vel. Donec vestibulum sed, vel euismod donec.</p>
      <p>Eros ante malesuada. Pellentesque senectus, a tempor et. At pellentesque. Molestie in, nonummy libero, justo eros pariatur. Tortor sed. A ac.</p>
      <p>In id, mauris viverra asperiores, bibendum in id.</p>
      <a class="btn">Read More</a>
    </article>
    <article class="article article-long">
      <div class="article-head"><h2>Relationships</h2><time>25.03.2010</time></div>
      <p style="margin-top:7px">A cras tincidunt, ut tellus et. Gravida scelerisque, ipsum sed iaculis, nunc non nam. Placerat sed phasellus, purus purus elit. Cras ante eros. Erat vel. Donec vestibulum sed, vel euismod donec.</p>
      <p>Eros ante malesuada. Pellentesque senectus, a tempor et. At pellentesque. Molestie in, nonummy libero, justo eros pariatur. Tortor sed. A ac.</p>
      <p>In id, mauris viverra asperiores, bibendum in id. Lorem ipsum dico oblique vis ex, pro id eruditi inermis, ei augue melius delicatissimi eos. Duo autem quaeque urbanitas an, ipsum intellegat ad cum, ea est populo suscipiantur Pellentesque senectus, a tempor et. At pellentesque. Molestie in, nonummy libero, justo eros pariatur. Tortor sed.</p>
      <p>A cras tincidunt, ut tellus et. Gravida scelerisque, ipsum sed iaculis, nunc non nam. Placerat sed phasellus, purus purus elit. Cras ante eros. Erat vel. Donec vestibulum sed, vel euismod donec.</p>
      <p>Eros ante malesuada. Pellentesque senectus, a tempor et. At pellentesque. Molestie in, nonummy libero, justo eros pariatur. Tortor sed. A ac.</p>
      <p>In id, mauris viverra asperiores, bibendum in id. Lorem ipsum dico oblique vis ex, pro id eruditi inermis, ei augue melius delicatissimi eos. Duo autem quaeque urbanitas an, ipsum intellegat ad cum, ea est populo suscipiantur.vituperatoribus. Has dico nonumy ubique ne, mel magna utinam feugait ei.</p>
      <a class="btn" style="margin-top:7px">Read More</a>
    </article>
  </main>

  <!-- Right column -->
  <section class="panel widget" style="left:530px;top:143px;width:148px;height:156px">
    <div class="widget-head"><span class="ornament" role="img" aria-label="Swirl ornament" style="left:-30px"></span><h2>Tag Cloud</h2></div>
    <div class="tag-cloud">
      Menopause Relationships<br>Experiences <b>News</b> Stories<br>Health Body Women<br>Menopause Relationships<br><b>Experiences</b> News Stories<br>Health Body Women<br><b>Menopause</b> Relationships<br><b>Experiences</b> News Stories<br>Health Body Women
    </div>
  </section>

  <section class="panel widget" style="left:530px;top:308px;width:148px;height:380px">
    <div class="widget-head"><span class="ornament" role="img" aria-label="Swirl ornament" style="left:-30px"></span><h2>Recent Posts</h2><span class="feed"></span></div>
    <div class="entry">Eros ante malesuada. Pellentesque senectus, a tempor et. At pellentesque. Molestie in, nonummy libero, justo eros pariatur. Tortor sed. A ac.<span class="more">Read More »</span></div>
    <div class="entry" style="padding-top:10px">In id, mauris viverra asperiores, bibendum in id. Eu molestie. Ac sit eu. Id iaculis id, pulvinar ut imperdiet. Vestibulum convallis. Gravida vivamus adipiscing, vitae ut ac, neque venenatis amet. Ultrices vestibulum purus.<span class="more">Read More »</span></div>
    <div class="entry" style="padding-top:10px">Eros ante malesuada. Pellentesque senectus, a tempor et. At pellentesque. Molestie in, nonummy libero, justo eros pariatur. Tortor sed. A ac.<span class="more">Read More »</span></div>
    <div class="entry" style="padding-top:10px">In id, mauris viverra asperiores, bibendum in id. Eu molestie. Ac sit eu. Id iaculis id, pulvinar ut imperdiet. Vestibulum convallis. Gravida vivamus adipiscing.<span class="more">Read More »</span></div>
    <div class="entry" style="padding-top:10px">Eros ante malesuada. Pellentesque senectus, a tempor et. At pellentesque.<span class="more">Read More »</span></div>
  </section>

  <section class="panel widget" style="left:530px;top:697px;width:148px;height:181px">
    <div class="widget-head"><span class="ornament" role="img" aria-label="Swirl ornament" style="left:-30px"></span><h2>Advertising</h2></div>
    <div class="ad-slot" role="img" aria-label="Advertisement: glass of water beside a Lunaveil moisturiser pack"></div>
  </section>

  <footer class="site-footer">
    <div class="footer-col" style="left:55px">
      <h3>Blog Archive</h3>
      <ul>
        <li>January 2009</li><li>February 2009</li><li>March 2009</li><li>April 2009</li><li>May 2009</li><li>June 2009</li><li>July 2009</li><li>August 2009</li><li>September 2009</li><li>Octomber 2009</li><li>November 2009</li>
      </ul>
    </div>
    <div class="footer-col" style="left:293px">
      <h3>Contact us</h3>
      <p>Feel free to contact us if you have any questions regarding your problems.<br>Email: info@velvetlarks.com<br>Phone: +123.456.789</p>
    </div>
    <div class="footer-col" style="left:530px">
      <h3>Send Your Story</h3>
      <p>Do you have a story you want to share with oter women? Send your story to us and we will publish it!</p>
    </div>
  </footer>
  <div class="footer-base"></div>
</div>
</body>
</html>
```